Nolvik Imaging Center web design and code

We need a new website for a Diagnostic Imaging Center in Fort Lauderdale, Florida.
The center has new RO advanced diagnostic equipment including a 3.0 Tesla MRI, a 128 slice PET/CT and a Varen T4 Ultrasound. Our facility has just been renovated and we have a lot of images, both facility and modality to use.
We have two client types, doctors who send their patients to our clinical Nolvik Center division, and clients who self-refer for screening studies to our Wellspire division. Both logos are attached. Please use the colors in the logos for the layout. Site should be coded in conventional HTML with CSS, but support multiple devices.
Updates

Reason: Waiting for additional designs. Most of the current designs are very similar in their structure and we would like more variety in terms of layout.

Target Market(s)

Doctors who refer patients for MRI, CT, PET, Bone Density and Ultrasound scans,
and
Retail clients who want full-body screening using MRI.

Industry/Entity Type

Medical Imaging

Coding

Coded - Design and coding required

Number of Pages Required

5+ page

Font styles to use
Sans Serif
Other font styles liked:
• Arquitecta

Requirements
Must have
• A good balance between color, shape, message and people/machine images.
• Must have images of the various machines, (RO Quillmark TN480, RO Quillmark 370, RO Varen T4) happy patients, clinical people, facility images and information about scans, preparations, costs, insurances we take.
• Must have links for social media and dynamic imagery.
Nice to have
• Some interactivity would be nice, including contact forms and scheduling application, Location map, directions, downloadable forms, history.
Should not have
• We do not want this to be built on WordPress platform. Should not be bound to a database platform that is proprietary or difficult to move.

```html
<!DOCTYPE html>
<html lang="en">
<head>
<meta charset="utf-8">
<title>Nolvik Imaging Center</title>
<link href="https://fonts.googleapis.com/css2?family=Open+Sans:wght@300;400;600;700&family=Noto+Serif:ital,wght@1,400&display=swap" rel="stylesheet">
<style>
:root{
  --green:#76a03a;
  --green-dark:#5d8428;
  --ink:#2b2b2b;
  --muted:#6b6b6b;
  --band:#0e0e0e;
  --panel-head:#3a3a3a;
  --footer:#2a2a2a;
  --footer-deep:#1d1d1d;
  --line:#dcdcdc;
  --white:#ffffff;
}
*{box-sizing:border-box;margin:0;padding:0}
html,body{width:1200px;height:2240px;overflow:hidden}
body{font-family:"Open Sans",Arial,sans-serif;color:var(--ink);background:var(--white);font-size:14px}
.wrap{width:960px;margin:0 auto;position:relative}

/* header */
.site-header{height:112px}
.site-header .wrap{height:112px;display:flex;align-items:center;justify-content:space-between}
.brand{display:flex;align-items:center;gap:14px}
.brand-mark{width:46px;height:46px;border-radius:50%;background:var(--green);flex:none}
.brand-name{font-size:24px;font-weight:700;line-height:1.05;color:var(--ink);text-transform:uppercase;width:230px}
.header-meta{text-align:right}
.header-contacts{display:flex;gap:26px;font-size:13px;color:var(--muted);justify-content:flex-end;align-items:center}
.header-contacts span{display:flex;align-items:center;gap:6px}
.btn{display:inline-block;background:var(--green);color:var(--white);font-weight:600;text-transform:uppercase;font-size:12px;padding:9px 18px;letter-spacing:.5px}
.header-meta .btn{margin-top:14px;background:#7f7f7f}

/* nav */
.main-nav{height:40px;background:var(--green)}
.main-nav ul{list-style:none;display:flex;height:40px;width:960px;margin:0 auto}
.main-nav li{color:var(--white);font-size:13px;font-weight:600;text-transform:uppercase;padding:0 22px;line-height:40px}
.main-nav li.active{background:var(--white);color:var(--green)}

/* hero */
.hero{height:428px;position:relative}
.hero-image{position:absolute;inset:0;background:linear-gradient(100deg,#9fb0b8 0%,#cfd8dc 35%,#e9eef0 60%,#f4f6f6 100%)}
.hero-caption{position:absolute;left:690px;top:120px;width:430px;font-family:"Noto Serif",Georgia,serif;font-style:italic;font-size:42px;line-height:1.2;color:var(--green)}
.hero-arrow{position:absolute;top:190px;width:36px;height:48px;background:rgba(30,30,30,.8);display:flex;align-items:center;justify-content:center}
.hero-arrow.prev{left:0}
.hero-arrow.next{right:0}

/* welcome */
.welcome{height:380px;padding-top:30px}
.welcome .wrap{display:flex;justify-content:space-between}
.welcome-text{width:470px;padding-top:30px}
.welcome-title{display:flex;align-items:center;gap:12px;font-size:30px;font-weight:300;margin-bottom:22px}
.welcome-title .brand-mark{width:34px;height:34px}
.welcome-title strong{font-size:20px;font-weight:700;text-transform:uppercase;line-height:1.05;width:180px}
.welcome-text p{font-size:13px;line-height:1.7;color:var(--muted);margin-bottom:18px}
.welcome-photo{width:460px;height:300px;background:linear-gradient(135deg,#e8dcd0,#c9a98e 55%,#f1ece6)}

/* equipment */
.equipment{height:420px;background:var(--band);padding-top:36px}
.section-title{color:var(--white);font-size:30px;font-weight:300;text-transform:uppercase;display:flex;align-items:center;gap:18px;margin-bottom:30px}
.section-title .rule{flex:1;height:1px;background:#444}
.section-title .brand-mark{width:28px;height:28px}
.equipment-list{display:flex;gap:32px;list-style:none}
.equipment-item{width:216px;text-align:center}
.equipment-photo{height:150px;border:4px solid #2f2f2f;background:linear-gradient(180deg,#f4f4f4,#c7cbcf)}
.equipment-item p{color:var(--white);font-size:12px;text-transform:uppercase;padding:12px 8px;line-height:1.45;min-height:56px}
.equipment-item.active{background:var(--green);padding:8px 8px 0}
.equipment-item.active .equipment-photo{border-color:var(--green-dark)}
.slider-dots{display:flex;gap:8px;justify-content:center;margin-top:22px}
.slider-dots i{width:9px;height:9px;border-radius:50%;background:#555}
.slider-dots i.on{background:var(--green)}

/* panels */
.panels{height:440px;padding-top:20px}
.panels .wrap{display:flex;gap:20px}
.panel{border:1px solid var(--line);box-shadow:0 2px 4px rgba(0,0,0,.12);height:380px;overflow:hidden}
.panel-head{background:var(--panel-head);color:var(--white);height:44px;display:flex;align-items:center;justify-content:space-between;padding:0 14px;font-size:20px;text-transform:uppercase}
.panel-head .btn{font-size:10px;padding:5px 8px}
.panel-head .brand-mark{width:22px;height:22px}
.stories{width:300px}
.story{display:flex;gap:12px;padding:16px 14px;border-bottom:1px solid var(--line)}
.story-photo{width:52px;height:110px;flex:none;background:linear-gradient(160deg,#d8c8b6,#a58e76)}
.story p,.news-item p{font-size:11px;line-height:1.5;color:var(--muted)}
.story strong,.news-item strong{display:block;color:var(--ink);font-size:12px;line-height:1.4;margin-bottom:3px}
.story em{color:var(--green);font-style:normal;font-size:11px}
.news{width:300px}
.news-item{padding:10px 14px;border-bottom:1px solid var(--line)}
.news-item time{display:block;font-size:10px;color:var(--green);margin-bottom:2px}
.news-item.active{background:var(--green)}
.news-item.active p,.news-item.active strong,.news-item.active time{color:var(--white)}
.inquiry{width:320px}
.inquiry form{padding:14px}
.inquiry label{display:block;font-size:12px;color:var(--muted);margin:6px 0 4px}
.inquiry .field{height:26px;border:1px solid var(--line)}
.inquiry .field.tall{height:80px}
.inquiry .btn{margin-top:12px;padding:7px 16px}

/* insurance */
.insurance{height:220px;background:var(--green);padding-top:36px}
.insurance .section-title .rule{background:rgba(255,255,255,.4)}
.insurer-row{display:flex;align-items:center;justify-content:space-between;margin-top:30px}
.insurer-list{display:flex;gap:46px;list-style:none}
.insurer{display:flex;align-items:center;gap:8px;color:var(--white);font-size:22px;font-weight:700}
.insurer i{width:14px;height:14px;background:var(--white)}

/* footer */
.site-footer{background:var(--footer);height:200px;color:#bdbdbd}
.site-footer .wrap{display:flex;gap:60px;padding-top:30px;height:172px}
.footer-col h4{color:var(--white);font-size:12px;text-transform:uppercase;margin-bottom:8px}
.footer-col ul{list-style:none;font-size:11px;line-height:1.6;columns:2;column-gap:30px}
.footer-col p{font-size:11px;line-height:1.6}
.newsletter-field{display:flex;margin-top:6px}
.newsletter-field span{width:150px;height:24px;background:var(--white)}
.newsletter-field b{background:var(--green);color:var(--white);font-size:10px;padding:5px 8px}
.footer-brand{margin-left:auto;display:flex;align-items:flex-start;gap:10px;color:#8a8a8a;font-weight:700;font-size:16px;text-transform:uppercase;line-height:1.1;width:190px;padding-top:20px}
.footer-brand .brand-mark{width:34px;height:34px;background:#777}
.copyright{background:var(--footer-deep);height:28px;line-height:28px;text-align:center;font-size:11px;color:#8a8a8a}
</style>
</head>
<body>

<header class="site-header">
  <div class="wrap">
    <div class="brand"><span class="brand-mark"></span><span class="brand-name">Nolvik Imaging Center</span></div>
    <div class="header-meta">
      <div class="header-contacts">
        <span><svg width="12" height="12" viewBox="0 0 24 24"><path fill="#76a03a" d="M6.6 10.8a15 15 0 0 0 6.6 6.6l2.2-2.2c.3-.3.7-.4 1-.2 1.1.4 2.3.6 3.6.6.6 0 1 .4 1 1V20c0 .6-.4 1-1 1A17 17 0 0 1 3 4c0-.6.4-1 1-1h3.5c.6 0 1 .4 1 1 0 1.3.2 2.5.6 3.6.1.3 0 .7-.2 1z"/></svg>(954) 555-0142</span>
        <span><svg width="13" height="10" viewBox="0 0 26 20"><rect x="1" y="1" width="24" height="18" fill="none" stroke="#76a03a" stroke-width="2"/><path d="M1 1l12 10L25 1" fill="none" stroke="#76a03a" stroke-width="2"/></svg>hello@nolvikimaging.com</span>
      </div>
      <span class="btn">Schedule Today</span>
    </div>
  </div>
</header>

<nav class="main-nav">
  <ul>
    <li class="active">Home</li><li>About Us</li><li>Stories</li><li>Exams</li><li>Wellspire</li><li>Insurance</li><li>Schedule</li><li>Contact Us</li>
  </ul>
</nav>

<section class="hero">
  <div class="hero-image" role="img" aria-label="Patient being positioned in an MRI scanner by a technologist"></div>
  <p class="hero-caption">Lorem ipsum dolor sit amet, consectetuer.</p>
  <span class="hero-arrow prev"><svg width="12" height="18" viewBox="0 0 12 18"><path d="M10 2L3 9l7 7" fill="none" stroke="#fff" stroke-width="3"/></svg></span>
  <span class="hero-arrow next"><svg width="12" height="18" viewBox="0 0 12 18"><path d="M2 2l7 7-7 7" fill="none" stroke="#fff" stroke-width="3"/></svg></span>
</section>

<section class="welcome">
  <div class="wrap">
    <div class="welcome-text">
      <h2 class="welcome-title">Welcome To <span class="brand-mark"></span><strong>Nolvik Imaging Center</strong></h2>
      <p>Our team is here to help you feel at ease before, during and after every scan. We combine modern imaging technology with caring staff so that your doctor receives clear, accurate results quickly and you receive a comfortable, calm experience from the moment you arrive.</p>
      <p>Our newly renovated facility in Fort Lauderdale offers MRI, PET/CT, CT, bone density and ultrasound studies under one roof, with flexible scheduling, friendly support and fast reporting for referring physicians and self-referred clients alike.</p>
      <span class="btn">Read More</span>
    </div>
    <div class="welcome-photo" role="img" aria-label="Smiling family of four sitting together on a sofa"></div>
  </div>
</section>

<section class="equipment">
  <div class="wrap">
    <h2 class="section-title">Advanced RO Diagnostic Imaging Systems <span class="rule"></span><span class="brand-mark"></span></h2>
    <ul class="equipment-list">
      <li class="equipment-item active"><div class="equipment-photo" role="img" aria-label="RO Quillmark TN480 MRI scanner"></div><p>RO Quillmark TN480</p></li>
      <li class="equipment-item"><div class="equipment-photo" role="img" aria-label="RO Quillmark 370 PET/CT scanner"></div><p>RO Quillmark 370 PET/CT</p></li>
      <li class="equipment-item"><div class="equipment-photo" role="img" aria-label="RO Varen T4 ultrasound machine"></div><p>High Resolution RO Varen T4 Ultrasound Machine</p></li>
      <li class="equipment-item"><div class="equipment-photo" role="img" aria-label="CT bone density scanner"></div><p>CT Bone Density</p></li>
    </ul>
    <div class="slider-dots"><i class="on"></i><i></i><i></i></div>
  </div>
</section>

<section class="panels">
  <div class="wrap">
    <div class="panel stories">
      <div class="panel-head">Stories <span class="btn">Tell Your Story</span></div>
      <div class="story"><div class="story-photo" role="img" aria-label="Portrait of a smiling older patient"></div><div><strong>Lorem ipsum dolor sit amet, consectetuer.</strong><p>Adipiscing elit, sed diam nonummy nibh euismod tincidunt ut laoreet dolore.</p><em>Read more</em></div></div>
      <div class="story"><div class="story-photo" role="img" aria-label="Portrait of a smiling young woman"></div><div><strong>Lorem ipsum dolor sit amet, consectetuer.</strong><p>Adipiscing elit, sed diam nonummy nibh euismod tincidunt ut laoreet dolore.</p><em>Read more</em></div></div>
    </div>
    <div class="panel news">
      <div class="panel-head">Latest News <span class="brand-mark"></span></div>
      <div class="news-item"><time>10 June 2024</time><strong>Lorem ipsum dolor sit amet, consectetuer.</strong><p>Sed diam nonummy nibh euismod.</p></div>
      <div class="news-item"><time>28 May 2024</time><strong>Lorem ipsum dolor sit amet, consectetuer.</strong><p>Sed diam nonummy nibh euismod.</p></div>
      <div class="news-item active"><time>14 May 2024</time><strong>Lorem ipsum dolor sit amet, consectetuer.</strong><p>Sed diam nonummy nibh euismod.</p></div>
      <div class="news-item"><time>02 May 2024</time><strong>Lorem ipsum dolor sit amet, consectetuer.</strong><p>Sed diam nonummy nibh euismod.</p></div>
    </div>
    <div class="panel inquiry">
      <div class="panel-head">Quick Inquiry <span class="brand-mark"></span></div>
      <form>
        <label>Name</label><div class="field"></div>
        <label>Phone</label><div class="field"></div>
        <label>Email</label><div class="field"></div>
        <label>Message</label><div class="field tall"></div>
        <span class="btn">Submit</span>
      </form>
    </div>
  </div>
</section>

<section class="insurance">
  <div class="wrap">
    <h2 class="section-title">Insurance We Accept <span class="rule"></span><span class="brand-mark" style="background:#fff"></span></h2>
    <div class="insurer-row">
      <svg width="16" height="26" viewBox="0 0 16 26"><path d="M13 2L3 13l10 11" fill="none" stroke="#fff" stroke-width="3"/></svg>
      <ul class="insurer-list">
        <li class="insurer"><i></i>Kestrel Health</li>
        <li class="insurer">Brightmoor</li>
        <li class="insurer">Selvane</li>
        <li class="insurer">Tallow Care</li>
        <li class="insurer">Orvina</li>
      </ul>
      <svg width="16" height="26" viewBox="0 0 16 26"><path d="M3 2l10 11L3 24" fill="none" stroke="#fff" stroke-width="3"/></svg>
    </div>
  </div>
</section>

<footer class="site-footer">
  <div class="wrap">
    <div class="footer-col"><h4>Quick Links</h4><ul><li>Home</li><li>About Us</li><li>Stories</li><li>Exams</li><li>Wellspire</li><li>Insurance</li><li>Schedule</li><li>Contact Us</li></ul></div>
    <div class="footer-col"><h4>Contact Details</h4><p>2810 Harbor Crest Ave,<br>Fort Lauderdale, FL<br>(954) 555-0142<br>hello@nolvikimaging.com</p></div>
    <div class="footer-col"><h4>Newsletter</h4><p>Get our updates in your inbox</p><div class="newsletter-field"><span></span><b>Subscribe</b></div></div>
    <div class="footer-brand"><span class="brand-mark"></span>Nolvik Imaging Center</div>
  </div>
  <div class="copyright">Copyright © 2024 Nolvik Imaging Center. All Rights Reserved.</div>
</footer>

</body>
</html>
```